Edgy rebranded biz cards KRB

We are rebranding our 20 yr old mortgage company with a new logo and would like cards to compliment our new look.

Target Market(s)

potential home buyers or clients for refinance

Industry/Entity Type

Mortgage Brokerage

Contact Information for Business Card

418 W. Lomita Ave #305
Henderson, NV 89152
702.519.4827 o
702-519-4829 f
www.kestrelridgelending,example
nmls 842019
KRB is an equal housing lender

Font styles to use
Sans Serif

Colors
0455a3
3176b5
0393ce
33a6d7

Requirements
Must have
• space for a photo
Nice to have
• One side with the company info and the other with the person's info

```html
<!DOCTYPE html>
<html lang="en">
<head>
<meta charset="utf-8">
<title>KRB Business Card</title>
<link href="https://fonts.googleapis.com/css2?family=Open+Sans:wght@400;600;700&family=Cousine&display=swap" rel="stylesheet">
<style>
  :root {
    --brand-deep: #0455a3;
    --brand-mid: #3176b5;
    --brand-bright: #0393ce;
    --brand-light: #33a6d7;
    --ink: #111111;
    --muted: #444444;
    --paper: #ffffff;
    --backdrop: #eef0f3;
  }
  html, body {
    margin: 0;
    padding: 0;
    width: 1200px;
    height: 1200px;
    overflow: hidden;
    background: var(--backdrop);
  }
  .canvas {
    position: relative;
    width: 1200px;
    height: 1200px;
  }
  .card {
    position: absolute;
    left: 50px;
    top: 285px;
    width: 1100px;
    height: 629px;
    background: var(--paper);
    box-shadow: 0 4px 18px rgba(0,0,0,0.12);
    overflow: hidden;
  }
  .brand-mark {
    position: absolute;
    left: 42px;
    top: 82px;
    display: flex;
    align-items: center;
    gap: 16px;
  }
  .brand-dot {
    width: 58px;
    height: 58px;
    border-radius: 50%;
    background: var(--brand-deep);
  }
  .brand-name {
    font-family: "Open Sans", sans-serif;
    font-weight: 700;
    font-size: 72px;
    line-height: 1;
    color: var(--brand-deep);
    letter-spacing: 2px;
  }
  .title-block {
    position: absolute;
    right: 60px;
    top: 58px;
    width: 500px;
    font-family: "Open Sans", sans-serif;
    color: var(--brand-deep);
  }
  .title-main {
    font-size: 86px;
    font-weight: 400;
    line-height: 1;
    letter-spacing: 6px;
    text-align: right;
  }
  .title-sub {
    margin-top: 6px;
    font-size: 30px;
    font-weight: 400;
    display: flex;
    justify-content: space-between;
    padding-left: 6px;
    padding-right: 2px;
  }
  .contact-list {
    position: absolute;
    left: 42px;
    top: 232px;
    font-family: "Cousine", monospace;
    color: var(--ink);
  }
  .contact-row {
    display: flex;
    align-items: flex-start;
    gap: 16px;
    margin-bottom: 14px;
  }
  .contact-icon {
    width: 40px;
    height: 40px;
    flex: none;
  }
  .contact-text {
    font-size: 34px;
    line-height: 40px;
    letter-spacing: 1px;
  }
  .contact-legal {
    margin-top: 6px;
    padding-left: 56px;
    font-family: "Open Sans", sans-serif;
    font-size: 20px;
    line-height: 26px;
    color: var(--muted);
  }
  .photo-space {
    position: absolute;
    right: 60px;
    top: 232px;
    width: 230px;
    height: 300px;
    background: linear-gradient(160deg, #d6ecf7 0%, #9fd0ea 100%);
    border: 4px solid var(--brand-light);
    box-sizing: border-box;
  }
  .footer-band {
    position: absolute;
    left: 0;
    bottom: 0;
    width: 100%;
    height: 43px;
    background: var(--brand-mid);
  }
</style>
</head>
<body>
<div class="canvas">
  <div class="card">
    <div class="brand-mark">
      <div class="brand-dot"></div>
      <div class="brand-name">KRB</div>
    </div>

    <div class="title-block">
      <div class="title-main">MORTGAGE</div>
      <div class="title-sub">
        <span>B</span><span>R</span><span>O</span><span>K</span><span>E</span><span>R</span><span>A</span><span>G</span><span>E</span>
      </div>
    </div>

    <div class="contact-list">
      <div class="contact-row phone-office">
        <svg class="contact-icon" viewBox="0 0 24 24" aria-hidden="true">
          <path fill="var(--brand-bright)" d="M6.6 10.8c1.4 2.8 3.8 5.1 6.6 6.6l2.2-2.2c.3-.3.7-.4 1-.2 1.1.4 2.3.6 3.6.6.6 0 1 .4 1 1V20c0 .6-.4 1-1 1C10.6 21 3 13.4 3 4c0-.6.4-1 1-1h3.5c.6 0 1 .4 1 1 0 1.3.2 2.5.6 3.6.1.3 0 .7-.2 1L6.6 10.8z"/>
        </svg>
        <span class="contact-text">702.519.4827 o</span>
      </div>

      <div class="contact-row phone-fax">
        <svg class="contact-icon" viewBox="0 0 24 24" aria-hidden="true">
          <g fill="none" stroke="var(--brand-bright)" stroke-width="1.8" stroke-linejoin="round">
            <rect x="3" y="9" width="18" height="9" rx="1.5"/>
            <path d="M7 9V3h10v6M7 15h10v6H7z"/>
          </g>
        </svg>
        <span class="contact-text">702-519-4829 f</span>
      </div>

      <div class="contact-row web">
        <svg class="contact-icon" viewBox="0 0 24 24" aria-hidden="true">
          <g fill="none" stroke="var(--brand-bright)" stroke-width="1.8">
            <circle cx="11" cy="12" r="9"/>
            <ellipse cx="11" cy="12" rx="4" ry="9"/>
            <line x1="2" y1="12" x2="20" y2="12"/>
            <line x1="4" y1="7" x2="18" y2="7"/>
            <line x1="4" y1="17" x2="18" y2="17"/>
          </g>
          <path fill="var(--brand-bright)" stroke="#fff" stroke-width="1" d="M13 12l10 4-4 1.5-1.5 4z"/>
        </svg>
        <span class="contact-text">www.kestrelridgelending,example</span>
      </div>

      <div class="contact-row address">
        <svg class="contact-icon" viewBox="0 0 24 24" aria-hidden="true">
          <path fill="none" stroke="var(--brand-bright)" stroke-width="1.6" stroke-linejoin="round" d="M2 12L12 3l10 9M5 9.5V21h5v-6h4v6h5V9.5M16 6V3.5h3v5"/>
        </svg>
        <span class="contact-text">418 W. Lomita Ave #305<br>Henderson, NV 89152</span>
      </div>

      <div class="contact-legal">nmls 842019 · KRB is an equal housing lender</div>
    </div>

    <div class="photo-space" role="img" aria-label="Space for the loan officer's portrait photo"></div>

    <div class="footer-band"></div>
  </div>
</div>
</body>
</html>
```